AN ELEGANT COSMETIC LABLE THAT CAN EASILY BE ALTERED TO FIT A VARIETY OF DIFFERENT PRODUCTS.

Predictable and ordinary designs are NOT welcome. Creative minds wanted.

Looking for a professional lable that is Canadian/USA Standard and compliant with the Personal Goods - Safety Statute in Onatrio. Which has a clean and elegant look, with a hint of holistic vibes.

This lable should be sleak and flexible to be altered to fit a variety of different products. Let your creativity come out with this project, the crazy and unpredictable are welcome.

This lable may be on the next biggest Cosmetic brand in the world. If you can see it, you can design it. All the best, looking forward to working with you.

Target Market(s)

Everyone who is looking for a clean natural lifestyle. The elite crowd.

Industry/Entity Type

Cosmetics

Font styles to use
Serif
Script

Colors

Designer to choose only greyscale colors for use in the design.

Requirements
Must have
• Company Name " VORELLI'S" and or Logo. See attachment
Nice to have
• One or more solid bars that can be colored to match the main product ingredient colour.
Should not have
• Too much different colors or images

```html
<!DOCTYPE html>
<html lang="en">
<head>
<meta charset="utf-8">
<title>Vorelli's Cosmetic Label System</title>
<link rel="stylesheet" href="https://fonts.googleapis.com/css2?family=Montserrat:wght@400;500;600;700&display=swap">
<style>
  :root {
    --bg: #ffffff;
    --ink: #1c1c1c;
    --paper: #f1f1f1;
    --amber: #f2c27a;
    --amber-soft: #fbeedb;
    --violet: #8e5fe6;
    --violet-soft: #e6dcfa;
    --grey: #c4c4c4;
    --grey-soft: #efefef;
    --teal: #5cc9c4;
    --teal-soft: #dcf3f2;
  }
  * { box-sizing: border-box; margin: 0; padding: 0; }
  html, body {
    width: 1200px; height: 953px; overflow: hidden;
    background: var(--bg);
    font-family: "Montserrat", sans-serif;
    color: var(--ink);
  }
  .canvas { position: relative; width: 1200px; height: 953px; }

  .label { position: absolute; overflow: hidden; }
  .label__pattern { position: absolute; inset: 0; }
  .label--amber .label__pattern { background: linear-gradient(135deg, var(--amber-soft), var(--amber) 50%, var(--amber-soft)); }
  .label--violet .label__pattern { background: linear-gradient(135deg, var(--violet-soft), var(--violet) 50%, var(--violet-soft)); }
  .label--grey .label__pattern { background: linear-gradient(135deg, var(--grey-soft), var(--grey) 50%, var(--grey-soft)); }
  .label--teal .label__pattern { background: linear-gradient(135deg, var(--teal-soft), var(--teal) 50%, var(--teal-soft)); }

  /* tall label */
  .label--tall { width: 300px; height: 520px; top: 40px; }
  .label--amber { left: 75px; }
  .label--violet { left: 450px; }
  .label--grey { left: 825px; }

  .panel {
    position: absolute; left: 34px; right: 34px; top: 52px; bottom: 40px;
    background: var(--paper);
    border: 2px solid var(--ink);
    display: flex; flex-direction: column;
  }
  .panel__brand {
    flex: 0 0 180px;
    display: flex; flex-direction: column; align-items: center; justify-content: center;
    border-bottom: 2px solid var(--ink);
  }
  .brand-mark {
    width: 46px; height: 46px; border: 3px solid var(--ink); margin-bottom: 16px;
  }
  .brand-name {
    font-weight: 500; font-size: 24px; letter-spacing: 3px; line-height: 1;
  }
  .brand-tagline {
    font-weight: 500; font-size: 7px; letter-spacing: 5px; margin-top: 6px;
  }
  .panel__row {
    flex: 1;
    display: flex; align-items: center; justify-content: center;
    border-bottom: 2px solid var(--ink);
    font-weight: 700; font-size: 12px; letter-spacing: 2px;
  }
  .panel__origin {
    flex: 0 0 30px;
    display: flex; align-items: center; justify-content: center;
    border-bottom: 2px solid var(--ink);
    font-weight: 700; font-size: 11px; letter-spacing: 2px;
  }
  .panel__meta { flex: 0 0 32px; display: flex; }
  .meta-volume {
    flex: 0 0 50%; background: var(--ink); color: var(--paper);
    display: flex; align-items: center; justify-content: center;
    font-weight: 700; font-size: 11px; letter-spacing: 2px;
  }
  .meta-expiry {
    flex: 1; display: flex; align-items: center; justify-content: center;
    font-weight: 700; font-size: 11px; letter-spacing: 2px;
  }

  /* wide jar label */
  .label--teal { left: 250px; top: 610px; width: 700px; height: 280px; }
  .panel--wide {
    left: 40px; right: 40px; top: 30px; bottom: 30px;
    display: grid;
    grid-template-columns: 45% 1fr;
    grid-template-rows: 1fr 1fr 40px;
  }
  .panel--wide .panel__brand {
    grid-row: 1 / 3; border-bottom: 2px solid var(--ink); border-right: 2px solid var(--ink);
  }
  .panel--wide .panel__row { font-size: 11px; }
  .panel__footer { grid-column: 1 / 3; display: flex; }
  .panel__footer .meta-volume { flex: 0 0 22%; }
  .panel__footer .footer-origin {
    flex: 1; display: flex; align-items: center; justify-content: center;
    border-right: 2px solid var(--ink);
    font-weight: 700; font-size: 11px; letter-spacing: 2px;
  }
  .panel__footer .meta-expiry { flex: 0 0 24%; }
</style>
</head>
<body>
<main class="canvas">

  <section class="label label--tall label--amber">
    <div class="label__pattern" role="img" aria-label="Amber geometric line pattern background"></div>
    <div class="panel">
      <div class="panel__brand">
        <div class="brand-mark"></div>
        <div class="brand-name">VORELLI'S</div>
        <div class="brand-tagline">MADE FOR YOU</div>
      </div>
      <div class="panel__row">COSMETICS PRODUCT</div>
      <div class="panel__row">FLOWER OIL / HONEY</div>
      <div class="panel__origin">MADE IN SOMEWHERE</div>
      <div class="panel__meta"><div class="meta-volume">100ML</div><div class="meta-expiry">EXP. DATE</div></div>
    </div>
  </section>

  <section class="label label--tall label--violet">
    <div class="label__pattern" role="img" aria-label="Violet geometric line pattern background"></div>
    <div class="panel">
      <div class="panel__brand">
        <div class="brand-mark"></div>
        <div class="brand-name">VORELLI'S</div>
        <div class="brand-tagline">MADE FOR YOU</div>
      </div>
      <div class="panel__row">COSMETICS PRODUCT</div>
      <div class="panel__row">FLOWER OIL / HONEY</div>
      <div class="panel__origin">MADE IN SOMEWHERE</div>
      <div class="panel__meta"><div class="meta-volume">100ML</div><div class="meta-expiry">EXP. DATE</div></div>
    </div>
  </section>

  <section class="label label--tall label--grey">
    <div class="label__pattern" role="img" aria-label="Grey geometric line pattern background"></div>
    <div class="panel">
      <div class="panel__brand">
        <div class="brand-mark"></div>
        <div class="brand-name">VORELLI'S</div>
        <div class="brand-tagline">MADE FOR YOU</div>
      </div>
      <div class="panel__row">COSMETICS PRODUCT</div>
      <div class="panel__row">FLOWER OIL / HONEY</div>
      <div class="panel__origin">MADE IN SOMEWHERE</div>
      <div class="panel__meta"><div class="meta-volume">100ML</div><div class="meta-expiry">EXP. DATE</div></div>
    </div>
  </section>

  <section class="label label--teal">
    <div class="label__pattern" role="img" aria-label="Teal geometric line pattern background"></div>
    <div class="panel panel--wide">
      <div class="panel__brand">
        <div class="brand-mark"></div>
        <div class="brand-name">VORELLI'S</div>
        <div class="brand-tagline">MADE FOR YOU</div>
      </div>
      <div class="panel__row">COSMETICS PRODUCT</div>
      <div class="panel__row">FLOWER OIL / HONEY</div>
      <div class="panel__footer">
        <div class="meta-volume">50GR</div>
        <div class="footer-origin">MADE IN SOMEWHERE</div>
        <div class="meta-expiry">EXP. DATE</div>
      </div>
    </div>
  </section>

</main>
</body>
</html>
```